Pelton|Marsh & Quillan business card contest

We need a logo for an upscale boutique diversified company involved in real estate, investments, cattle, and more. Our businesses DO NOT need to be reflected in the business card nor do we want them noted. This is our logo and colors and we love our logo and colors. Our logo looks best against a black background and we like to include the firm name in our logo usage. importantly, the names Pelton and Marsh are separated by | not / and we use an ampersand not the word and.
On the front of the card, we want to include:
company logo and name (Pelton|Marsh & Quillan)
on the back, we would definitely include:
address, email, cell #
logo and name (smaller size than front)

The variable will be location of individual name and title (mine for example is ) - whether on the front OR on the back. interested in variations from which to choose
Dr. Neil R. Whitcombe, CFA
Scientifique des Fusées Financières

we would like to use contemporary symbols for address, email address, cell # with an option for web site that we do not intend to use initially. we like two sided cards and believe this design should use four rounded corners with the standard size. we prefer thicker card stock and may look at metal.

```html
<!DOCTYPE html>
<html lang="en">
<head>
<meta charset="utf-8">
<title>Pelton|Marsh &amp; Quillan — Business Card</title>
<link rel="stylesheet" href="https://fonts.googleapis.com/css2?family=Poppins:wght@300;400&display=swap">
<style>
  :root {
    --backdrop: #2b2b2d;
    --card: #121212;
    --frame: #e8e8e8;
    --accent: #d8730f;
    --text: #e2e2e2;
    --muted: #8a8a8a;
    --rule: #555555;
  }
  * { box-sizing: border-box; margin: 0; padding: 0; }
  html, body {
    width: 1200px; height: 874px; overflow: hidden;
    background: var(--backdrop);
    font-family: "Poppins", sans-serif;
  }
  .stage {
    width: 1200px; height: 874px;
    display: flex; flex-direction: column; align-items: center; justify-content: center;
    gap: 34px;
  }
  .card {
    position: relative;
    width: 640px; height: 366px;
    background: var(--card);
    border-radius: 4px;
    box-shadow: 0 8px 22px rgba(0,0,0,.45);
  }
  .card__frame {
    position: absolute; inset: 14px;
    border: 2px solid var(--frame);
  }
  .card__body {
    position: absolute; inset: 0;
    display: flex; flex-direction: column; align-items: center; justify-content: center;
  }
  .brand {
    display: flex; align-items: center; gap: 14px;
  }
  .brand__mark {
    width: 30px; height: 30px; background: var(--accent);
  }
  .brand__name {
    font-weight: 300; font-size: 30px; letter-spacing: .5px; color: var(--muted);
  }
  .contact { width: 330px; }
  .contact__name {
    color: var(--accent); font-weight: 400; font-size: 21px; line-height: 1.2;
  }
  .contact__credential { font-size: 11px; margin-left: 3px; }
  .contact__title {
    color: var(--text); font-weight: 300; font-size: 15px; margin-top: 2px;
  }
  .contact__rule {
    height: 1px; background: var(--rule); margin: 8px 0;
  }
  .contact__line {
    color: var(--text); font-weight: 300; font-size: 14px; line-height: 1.6;
  }
</style>
</head>
<body>
<main class="stage">
  <section class="card card--front">
    <div class="card__frame"></div>
    <div class="card__body">
      <div class="brand">
        <span class="brand__mark"></span>
        <span class="brand__name">Pelton|Marsh &amp; Quillan</span>
      </div>
    </div>
  </section>

  <section class="card card--back">
    <div class="card__frame"></div>
    <div class="card__body">
      <div class="contact">
        <p class="contact__name">Dr. Neil R. Whitcombe,<span class="contact__credential">CFA</span></p>
        <p class="contact__title">Scientifique des Fusées Financières</p>
        <div class="contact__rule"></div>
        <p class="contact__line">2418 Larkspur Court, Juneau, Alaska 99801</p>
        <p class="contact__line">M- 907-448-3172 E-info@peltonmarshquillan.com</p>
        <div class="contact__rule"></div>
        <p class="contact__line">www.peltonmarshquillan.com</p>
      </div>
    </div>
  </section>
</main>
</body>
</html>
```